New business Card Design

I'm looking to do a new design for our business cards.

Our Company its called the Garden quarter we are a High end outdoor Design and construction company based out of miami FL

Our Style is elegant, minimalist, Luxury but accessible.

see our Website: www.thegardenquarter-example.com

Attached find our logo as well as some samples the cards that we have for our sister company.

Sample Contact information ( in no particular order):

Marco Ventresca
VP of Sales and Marketing
Marco@thegardenquarter-example.com
555.204.7719
4172 NW 63 AVE Miami Florida, 33199

Designs are Looking Great guys but not quite there yet!

Upload your last few designs between today and Tomorrow. we will be choosing one on Saturday!

Cheers, 

Marco Ventresca
Director Of Marketing 

Hello Guys, 

Sorry we have not made a decision yet.  a lot of cool stuff! just narrowing down our options. 
expect a decision with in a day or 2. 

Marco. 

Target Market(s)

high End Design and construction. Luxurious but accessible

Industry/Entity Type

Construction

Colors

Designer to choose colors to be used in the design.

```html
<!DOCTYPE html>
<html lang="en">
<head>
<meta charset="utf-8">
<title>The Garden Quarter — Business Card</title>
<link href="https://fonts.googleapis.com/css2?family=Exo+2:wght@400;500;600;700&display=swap" rel="stylesheet">
<style>
  :root {
    --bg: #e9e6e0;
    --card-white: #ffffff;
    --card-shade: #e4e5e7;
    --brand-blue: #1a8fd0;
    --brand-blue-dark: #0f6fae;
    --brand-green: #5bb83a;
    --band-grey: #d3d5d8;
    --ink: #3a3d42;
    --ink-soft: #7a7e85;
    --white: #ffffff;
  }
  * { box-sizing: border-box; margin: 0; padding: 0; }
  html, body { width: 1057px; height: 1200px; overflow: hidden; }
  body {
    background: var(--bg);
    font-family: "Exo 2", Arial, sans-serif;
    position: relative;
  }
  .card {
    position: absolute;
    left: 108px;
    width: 840px;
    height: 480px;
    background: radial-gradient(ellipse at 55% 40%, var(--card-white) 0%, var(--card-shade) 100%);
    box-shadow: 0 10px 28px rgba(0,0,0,0.18);
    overflow: hidden;
  }
  .card--front { top: 90px; }
  .card--back { top: 630px; }

  .front-frame {
    position: absolute; inset: 0;
    border: 22px solid var(--brand-blue);
  }
  .front-frame::after {
    content: ""; position: absolute; inset: 0;
    border: 6px solid var(--brand-blue-dark);
  }

  .brand { position: absolute; display: flex; align-items: center; gap: 16px; white-space: nowrap; }
  .brand__dot {
    width: 58px; height: 58px; border-radius: 50%;
    background: var(--brand-blue); flex: none;
  }
  .brand__name {
    font-weight: 600; color: var(--ink);
    font-size: 34px; letter-spacing: 1px; line-height: 1; text-transform: uppercase;
  }
  .brand__tagline {
    font-weight: 500; color: var(--ink-soft);
    font-size: 11.5px; letter-spacing: 4px; text-transform: uppercase; margin-top: 7px;
  }
  .card--front .brand { left: 50%; top: 50%; transform: translate(-50%, -50%); }
  .card--back .brand { left: 44px; top: 120px; }
  .card--back .brand__name { font-size: 30px; }
  .card--back .brand__dot { width: 52px; height: 52px; }

  .back-shapes { position: absolute; inset: 0; }

  .holder { position: absolute; left: 40px; top: 316px; color: var(--white); }
  .holder__name { font-weight: 700; font-size: 28px; letter-spacing: 1.5px; text-transform: uppercase; line-height: 1; }
  .holder__role { font-weight: 500; font-size: 17px; letter-spacing: 1px; text-transform: uppercase; margin-top: 6px; }

  .contact { position: absolute; list-style: none; }
  .contact li { display: flex; align-items: center; gap: 10px; font-size: 13.5px; line-height: 1; margin-bottom: 10px; white-space: nowrap; }
  .contact__icon { width: 16px; height: 16px; background: var(--brand-green); flex: none; display: flex; align-items: center; justify-content: center; }
  .contact--blue { left: 40px; top: 392px; color: var(--white); }
  .contact--grey { left: 540px; top: 318px; color: var(--ink); font-weight: 600; }
  .contact--grey li { font-size: 15px; margin-bottom: 14px; }
</style>
</head>
<body>

  <section class="card card--front">
    <div class="front-frame"></div>
    <div class="brand">
      <span class="brand__dot"></span>
      <div>
        <div class="brand__name">The Garden Quarter</div>
        <div class="brand__tagline">Outdoor Design &amp; Construction</div>
      </div>
    </div>
  </section>

  <section class="card card--back">
    <svg class="back-shapes" width="840" height="480" viewBox="0 0 840 480">
      <polygon points="300,266 840,266 840,300 290,300" fill="var(--brand-green)"/>
      <polygon points="490,300 840,300 840,392 462,392" fill="var(--band-grey)"/>
      <polygon points="0,300 490,300 430,480 0,480" fill="var(--brand-blue)"/>
      <polygon points="0,300 490,300 480,330 0,330" fill="var(--brand-blue-dark)" opacity="0.25"/>
    </svg>

    <div class="brand">
      <span class="brand__dot"></span>
      <div>
        <div class="brand__name">The Garden Quarter</div>
        <div class="brand__tagline">Outdoor Design &amp; Construction</div>
      </div>
    </div>

    <div class="holder">
      <div class="holder__name">Marco Ventresca</div>
      <div class="holder__role">Founder</div>
    </div>

    <ul class="contact contact--blue">
      <li><span class="contact__icon"><svg width="10" height="10" viewBox="0 0 10 10"><path d="M5 0.5a3 3 0 0 0-3 3c0 2.3 3 6 3 6s3-3.7 3-6a3 3 0 0 0-3-3z" fill="#fff"/></svg></span>4172 NW 63 AVE Miami Florida, 33199</li>
      <li><span class="contact__icon"><svg width="10" height="10" viewBox="0 0 10 10"><circle cx="5" cy="5" r="4" fill="none" stroke="#fff" stroke-width="1.2"/><path d="M1 5h8M5 1v8" stroke="#fff" stroke-width="1"/></svg></span>www.thegardenquarter-example.com</li>
      <li><span class="contact__icon"><svg width="10" height="10" viewBox="0 0 10 10"><rect x="1" y="2" width="8" height="6" fill="none" stroke="#fff" stroke-width="1.2"/><path d="M1 2l4 3 4-3" fill="none" stroke="#fff" stroke-width="1"/></svg></span>Marco@thegardenquarter-example.com</li>
    </ul>

    <ul class="contact contact--grey">
      <li><span class="contact__icon"><svg width="10" height="10" viewBox="0 0 10 10"><path d="M2 1l2 0 1 2-1.2 1a5 5 0 0 0 2.2 2.2L7 5l2 1v2c-4 0.5-8-3.5-7-7z" fill="#fff"/></svg></span>555.204.7719</li>
      <li><span class="contact__icon"><svg width="10" height="10" viewBox="0 0 10 10"><path d="M2 1l2 0 1 2-1.2 1a5 5 0 0 0 2.2 2.2L7 5l2 1v2c-4 0.5-8-3.5-7-7z" fill="#fff"/></svg></span>555.204.7719</li>
    </ul>
  </section>

</body>
</html>
```